Microlight Aircraft Website Project

Need a website designed, or at least a template made, that my web programmer can work with here. We are a new manufacturer of microlight aircraft & powered hang gliders. Our company name is Brisk Fern. We manufacture portable utility aircraft in the Light Sport category (formerly known as Ultralights or Microlights). Our particular design is a 2-seat powered hang glider and caters to those who want to go explore the backcountry. We are not necessarily aviation nuts, but more into the development of a flying utility vehicle for extreme exploration and expeditions. We have been importing these aircraft from 3 countries for 15 years and have supplied over 200 expedition-quality aircraft world-wide. We are now manufacturing here in the US.

Industry/Entity Type

Manufacturer

Coding

Coded - Design and coding required

```html
<!DOCTYPE html>
<html lang="en">
<head>
<meta charset="utf-8">
<title>Brisk Fern</title>
<link href="https://fonts.googleapis.com/css2?family=Chakra+Petch:wght@300;400;600&display=swap" rel="stylesheet">
<style>
:root{
  --sky-top:#858c95;
  --sky-low:#9aa0a3;
  --haze:#a3a8a6;
  --hills:#6b717d;
  --hills-dark:#5d6470;
  --field-far:#9a9d86;
  --field-light:#a7a684;
  --field-mid:#838c6c;
  --field-near:#6e7a57;
  --trees:#3f4a33;
  --shade:rgba(40,45,50,0.18);
  --text:#ffffff;
  --nav-text:#eef0f2;
  --rule:rgba(255,255,255,0.85);
}
*{margin:0;padding:0;box-sizing:border-box}
html,body{width:1200px;height:1000px;overflow:hidden}
body{font-family:"Chakra Petch",sans-serif;color:var(--text);background:var(--sky-top)}
.hero{position:relative;width:1200px;height:1000px;overflow:hidden}
.hero-photo{position:absolute;inset:0;
  background:
    radial-gradient(ellipse 420px 90px at 760px 955px,var(--trees) 0%,rgba(63,74,51,0.6) 55%,rgba(63,74,51,0) 100%),
    radial-gradient(ellipse 360px 70px at 1050px 870px,rgba(63,74,51,0.7) 0%,rgba(63,74,51,0) 100%),
    radial-gradient(ellipse 520px 180px at 220px 600px,rgba(190,185,150,0.45) 0%,rgba(190,185,150,0) 100%),
    radial-gradient(ellipse 380px 40px at 300px 492px,rgba(80,88,80,0.55) 0%,rgba(80,88,80,0) 100%),
    radial-gradient(ellipse 700px 60px at 820px 350px,var(--hills-dark) 0%,rgba(93,100,112,0) 100%),
    linear-gradient(to bottom,
      var(--sky-top) 0%,
      var(--sky-low) 28%,
      var(--haze) 33%,
      var(--hills) 37%,
      var(--hills) 39%,
      var(--haze) 42%,
      var(--field-far) 46%,
      var(--field-light) 58%,
      var(--field-mid) 72%,
      var(--field-near) 88%,
      var(--field-near) 100%);}
.hero-shade{position:absolute;inset:0;background:var(--shade)}
.brand{position:absolute;top:62px;left:0;width:1200px;text-align:center}
.brand-name{display:inline-flex;align-items:center;gap:10px;font-size:22px;font-weight:600;letter-spacing:2.4px;text-transform:uppercase;color:var(--text)}
.brand-mark{width:12px;height:12px;background:var(--text)}
.main-nav{position:absolute;top:174px;left:210px;width:779px;height:30px;border-bottom:1px solid var(--rule)}
.main-nav ul{list-style:none;position:relative;height:100%}
.main-nav li{position:absolute;top:0;font-size:14px;font-weight:300;letter-spacing:2.5px;color:var(--nav-text)}
.nav-home{left:98px}.nav-about{left:240px}.nav-aircraft{left:420px}.nav-contact{left:610px}
.tagline{position:absolute;top:516px;left:0;width:1200px;text-align:center}
.tagline h1{font-size:49px;font-weight:300;letter-spacing:0.4px;line-height:1.1}
.tagline-rule{position:absolute;top:66px;left:424px;width:313px;height:1px;background:var(--rule)}
</style>
</head>
<body>
<main class="hero">
  <div class="hero-photo" role="img" aria-label="Powered hang glider with a long blue wing and a pilot flying low over misty green farmland, mountains on the horizon"></div>
  <div class="hero-shade"></div>
  <header class="brand">
    <span class="brand-name"><span class="brand-mark"></span>Brisk Fern</span>
  </header>
  <nav class="main-nav">
    <ul>
      <li class="nav-home">HOME</li>
      <li class="nav-about">ABOUT US</li>
      <li class="nav-aircraft">AIRCRAFTS</li>
      <li class="nav-contact">CONTACT</li>
    </ul>
  </nav>
  <section class="tagline">
    <h1>My soul is in the sky</h1>
    <span class="tagline-rule"></span>
  </section>
</main>
</body>
</html>
```